Stationary Set and Logo Update **PAYMENT GUARANTEED**

Stationery Design and Logo Update

About Us

Trindex Supply is a wholesale distributor of OEM [original brand] and compatible [generic brand] parts and supplies for use in copiers, faxes, printers, and multi-function machines. In plain English…we sell all the parts and supplies [such as toner] that make up any office equipment which outputs an image on paper.

Trindex was the 1st distributor to develop and sell a generic brand copier part in the United States. We have been in business since 1972 [nearly 40 years]. Our tagline is "The Steady Choice," as in our company was the first alternative product that copier dealers had to buying original brand copier parts. Trindex is known for offering reliable and cost-effective OEM and compatible products.

Project

We require a fresh, modern and corporate identity. Please submit a stationary package inclusive of a double-sided business card (2" x 3.5"), letterhead (8.5'x11"), and standard #10 envelope (4-1/8” x 9-1/2). You may use our current logo or preferably your take on an updated one. If an attempt is made in updating the logo #004D8E or a similar hue should be used as the primary color.

The design should be clean, simple, modern and professional and make an immediate impact.

Target Market(s)

Copier and printer dealers who lease and service imaging equipment in the United States and Latin America.

Industry/Entity Type

Business

Requirements
Must have
• Simple, clean, modern and professional. Please use #004D8E or a similar hue as the primary color. Letterhead must accommate (2) addresses. We have 2 locations.
Nice to have
• A simple, modern update to our current logo. https://assets.mailvorbo.example/fs030/5520384417702/img/418.jpg
Should not have
• More than (2) colors on logo.

```html
<!DOCTYPE html>
<html lang="en">
<head>
<meta charset="utf-8">
<title>Trindex Supply Letterhead</title>
<link rel="stylesheet" href="https://fonts.googleapis.com/css2?family=Open+Sans:wght@400;600;700&display=swap">
<style>
  :root {
    --brand-navy: #1b3f7f;
    --pattern-tone: #4a689c;
    --ink: #1a1a1a;
    --paper: #ffffff;
    --stage: #ffffff;
  }
  * { margin: 0; padding: 0; box-sizing: border-box; }
  html, body { width: 1200px; height: 900px; overflow: hidden; background: var(--stage); }
  body { position: relative; font-family: "Open Sans", Arial, sans-serif; color: var(--ink); }

  .sheet { position: absolute; width: 562px; height: 728px; }
  .sheet--back { left: 373px; top: 48px; background: var(--pattern-tone); }
  .sheet--front { left: 256px; top: 108px; background: var(--paper); overflow: hidden; }

  .brand { position: absolute; left: 40px; top: 64px; width: 148px; }
  .brand__row { display: flex; align-items: center; gap: 6px; }
  .brand__dot { width: 16px; height: 16px; border-radius: 50%; background: var(--brand-navy); }
  .brand__name { font-size: 30px; font-weight: 700; color: var(--brand-navy); line-height: 1; }
  .brand__tagline { margin-top: 6px; font-size: 5.5px; letter-spacing: 1.4px; text-transform: uppercase; color: var(--brand-navy); text-align: right; }

  .office { position: absolute; top: 78px; font-size: 7px; line-height: 8.2px; color: #333; padding-left: 8px; }
  .office::before { content: ""; position: absolute; left: 0; top: 2px; width: 4px; height: 4px; border-radius: 50%; background: var(--brand-navy); }
  .office__title { font-weight: 700; color: var(--ink); }
  .office--corporate { left: 210px; }
  .office--west { left: 327px; }

  .letter { position: absolute; left: 61px; top: 186px; width: 430px; font-size: 10.4px; line-height: 12.6px; }
  .letter p { margin-bottom: 12.6px; }
  .letter .indent { text-indent: 32px; }
  .recipient { margin-bottom: 26px !important; }
  .signature { margin-top: 38px; }

  .corner-accent { position: absolute; }
  .corner-accent--left { left: 0; bottom: 0; width: 125px; height: 100px;
    background: radial-gradient(ellipse at 0% 100%, var(--brand-navy) 0%, rgba(27,63,127,0.55) 40%, rgba(27,63,127,0) 75%); }
  .corner-accent--right { right: 0; bottom: 0; width: 72px; height: 46px;
    background: radial-gradient(ellipse at 100% 100%, var(--brand-navy) 0%, rgba(27,63,127,0.5) 40%, rgba(27,63,127,0) 75%); }
</style>
</head>
<body>
  <div class="sheet sheet--back" role="img" aria-label="Reverse side of letterhead covered in a navy bubble pattern"></div>

  <div class="sheet sheet--front">
    <div class="brand">
      <div class="brand__row">
        <span class="brand__dot"></span>
        <span class="brand__name">Trindex</span>
      </div>
      <div class="brand__tagline">The Steady Choice</div>
    </div>

    <div class="office office--corporate">
      <div class="office__title">Corporate Office</div>
      2280 Harbor Point Avenue<br>
      Coral Bend, FL 33019<br>
      Local: 555.014.2230<br>
      Fax: 555.014.2291
    </div>

    <div class="office office--west">
      <div class="office__title">Trindex West</div>
      West Coast Fulfillment Center<br>
      Sage Ridge Industrial Park #2<br>
      4417 Talvo Way<br>
      Dry Creek, NV 89502<br>
      Toll Free: 800.555.0148
    </div>

    <div class="letter">
      <p class="recipient">Umsandreet nons a<br>&nbsp;ad dignibh el irilismolore<br>magna core mod<br>te te feuiscilisi.</p>
      <p>Idunt at digniat. Ut</p>
      <p>euisl dio od ming eugue magna facidunt ing et aliscilit, verci et adionsenit velessi ex ex eseniatie magna feum niam zzriustisl dipismodolut praestrud doluptat. Lesed modigna feugait dolestio exerit landit lan esequamcommy non ullam ing ex et illa augait, consequ iscillam duis aliquat.</p>
      <p class="indent">Min velit doluptat. Dio odiat. Min henit vullan erit luptat, vercilit prat, sis doloreet ing eugiamcons num ipit nit, sectet nostrud elit aciliscil eugue tisl ex el ute feuis nullam doloborper inis acidunt adionse quamet velissi. Modio dolor si te dolortis nim at am veniam do esectem zzriusto od modit am quisit wisl er summy nim.</p>
      <p class="indent">Quis dit non utet veniat alit amcon henit la corem do odit lutpat, cor aut am zzrit ipsusto conse duis eummy non exerostrud te conum iure dolorer sim exeriure essi bla feugiam eum iriusto eum ea amcommolore dunt doluptat aliquam iriustrud ectem zzrit velendit volessim verostie conulluptat.</p>
      <p>Sincerely</p>
      <p class="signature">Lorna Aveline<br>Marketing Coordinator</p>
    </div>

    <div class="corner-accent corner-accent--left" role="img" aria-label="Cluster of navy bubbles in the lower left corner"></div>
    <div class="corner-accent corner-accent--right" role="img" aria-label="Small cluster of navy bubbles in the lower right corner"></div>
  </div>
</body>
</html>
```